Vantrell Brightpaths

Need to improve polish and professionalism of PPT presentation. Get consistent look and feel through whole slides, improved look and feel while maintaining the corporate standards/colour scheme, from the Quenbrook corporate presentation. Need everything in Arial font with colours consistent with the PPT template

```html
<!DOCTYPE html>
<html lang="en">
<head>
<meta charset="utf-8">
<title>Vantrell Brightpaths – KPIs &amp; Production Fundamentals deck</title>
<link href="https://fonts.googleapis.com/css2?family=Arimo:wght@400;700&display=swap" rel="stylesheet">
<style>
:root{
  --ink:#12262b;
  --ink-2:#1d3439;
  --red:#d7262e;
  --steel:#9aa3a9;
  --steel-2:#b7bec2;
  --green:#3c8a2e;
  --yellow:#f3e500;
  --plum:#6b1f5a;
  --canvas:#a9a9a9;
  --text:#2a2a2a;
}
*{box-sizing:border-box;margin:0;padding:0}
html,body{width:947px;height:1200px;overflow:hidden}
body{background:var(--canvas);font-family:Arimo,Arial,sans-serif;color:var(--text)}
.deck{display:grid;grid-template-columns:repeat(4,220px);grid-auto-rows:124px;column-gap:5px;row-gap:4.6px;padding:24px 0 0 26px}
.slide{position:relative;background:#fff;overflow:hidden}
.slide.std::before{content:"";position:absolute;left:4px;top:12px;width:6px;height:5px;background:var(--ink);z-index:3}
.ttl{position:absolute;left:17px;top:10px;font-size:6.6px;font-weight:700;color:var(--red);line-height:1.15;z-index:3}
.sub{position:absolute;font-size:3px;line-height:1.3;z-index:3}
.sub b{font-weight:700}
.foot{position:absolute;left:0;right:0;bottom:0;height:8px;background:var(--ink);display:flex;align-items:center;z-index:4}
.brand{color:#fff;font-size:4px;font-weight:700;letter-spacing:.35px;margin-left:10px}
.legal{color:#8d9ca1;font-size:2px;margin-left:58px}
.pg{position:absolute;right:8px;top:0;width:6px;height:8px;background:var(--red);color:#fff;font-size:2.2px;font-style:normal;display:grid;place-items:center}
.bul{position:absolute;list-style:none;font-size:2.5px;line-height:1.35;z-index:3}
.bul li{position:relative;padding-left:5px;margin-top:.6px}
.bul li::before{content:"+";position:absolute;left:0;top:-.6px;color:var(--red);font-weight:700;font-size:3.6px}
.bul li.gap{margin-top:3px}
.bul li.sm{padding-left:9px;font-size:2px}
.bul li.sm::before{left:5px;font-size:2.6px}
.photo{position:absolute;top:0;right:0;bottom:8px;width:56%;background:linear-gradient(165deg,#d1d8da 0%,#8a999d 45%,#3f4e52 100%);overflow:hidden}
.photo::before{content:"";position:absolute;left:-34%;top:-25%;width:58%;height:150%;border-radius:50%;background:#fff}
.photo.night{width:60%;background:linear-gradient(160deg,#263538,#0f1b1e 70%)}
.dark{background:linear-gradient(150deg,#2a3a3d 0%,#142225 55%,#0c1518 100%)}
.sec-h{position:absolute;left:19px;top:45px;font-size:8.4px;color:#c9cfd1;letter-spacing:.2px;line-height:1.2}
.sec-s{position:absolute;left:19px;font-size:6.4px;color:var(--red);font-weight:700;line-height:1.25}
.logo-line{position:absolute;display:flex;align-items:center;gap:2px;color:#fff;font-weight:700}
.logo-line i{display:block;width:3px;height:3px;background:var(--red)}
.tum{position:absolute;left:16px;top:26px;width:189px;height:36px}
.org{position:absolute;left:5px;width:110px;height:32px;z-index:3}
.flow{position:absolute;display:flex;align-items:center;gap:1.5px;z-index:3}
.box{background:var(--steel);color:#fff;font-size:2.2px;line-height:1.3;padding:2.5px;border-radius:2px;display:flex;align-items:center}
.arw{flex:none;width:5px;height:5px;border-radius:50%;border:.5px solid var(--red);color:var(--red);font-size:3.4px;line-height:1;display:grid;place-items:center;font-weight:700}
.arw.plain{border:0}
.step-h{position:absolute;left:17px;top:10px;font-size:6.2px;color:var(--red);font-weight:700;line-height:1.1}
.step-tag{position:absolute;left:17px;top:19px;height:7.5px;width:30px;background:var(--red);color:#fff;font-size:5.4px;font-weight:700;padding-left:7px;line-height:7.5px;clip-path:polygon(0 0,100% 0,88% 100%,0 100%)}
.step-ico{position:absolute;left:18px;top:30px;width:10px;height:10px;border-radius:50%;background:var(--ink);box-shadow:inset 0 0 0 1.6px var(--ink),inset 0 0 0 2.2px #fff}
.step-t{position:absolute;left:35px;top:32px;font-size:3.8px;font-weight:700;line-height:1.25}
.step-q{position:absolute;left:35px;font-size:3.6px;font-weight:700;line-height:1.3}
.step-e{position:absolute;left:35px;font-size:3px}
.obj{position:absolute;left:17px;display:flex;align-items:center;gap:6px;font-size:2.3px;line-height:1.35;z-index:3}
.obj span{display:block;width:10px;height:10px;border-radius:50%;background:var(--red);flex:none}
.vm-h{position:absolute;left:17px;top:26px;font-size:2.6px;font-weight:700}
.ico{position:absolute;width:13px;height:13px;border-radius:50%;border:.6px solid #555}
/* bottleneck slides */
.bn-art{position:absolute;left:28px;top:41px;width:166px;height:35px;border-radius:10px;background:linear-gradient(180deg,#f2f4f4 0%,#dfe5e4 55%,#c9d8c6 100%)}
.bn-cap{position:absolute;font-size:4.4px;line-height:1.2;display:flex;gap:1.6px;z-index:3}
.bn-cap i{flex:none;width:4.8px;height:4.8px;border-radius:50%;background:var(--red);color:#fff;font-style:normal;font-size:3px;display:grid;place-items:center;margin-top:-.3px}
.bn-tag{position:absolute;top:77px;height:3.6px;background:var(--red);color:#fff;font-size:2.3px;line-height:3.6px;text-align:center;white-space:nowrap;z-index:3}
</style>
</head>
<body>
<svg width="0" height="0" style="position:absolute" aria-hidden="true">
  <defs>
    <symbol id="tum-base" viewBox="0 0 190 36">
      <rect width="190" height="36" fill="#9aa3a9"/>
      <rect x="6" y="2.2" width="177.7" height="5.6" fill="#12262b"/>
      <text x="95" y="5.9" font-size="2.4" fill="#fff" text-anchor="middle" font-family="Arimo,Arial,sans-serif">Calendar Time</text>
    </symbol>
    <symbol id="tum-avail" viewBox="0 0 190 36">
      <g font-family="Arimo,Arial,sans-serif" font-size="2.4" fill="#fff" text-anchor="middle">
        <rect x="6" y="9" width="118.3" height="5.6" fill="#12262b"/><text x="65" y="12.6">Available Time</text>
        <rect x="124.3" y="9" width="59.4" height="3.4" fill="#a31d23"/><text x="154" y="11.5" font-size="2">Down</text>
        <rect x="124.3" y="12.9" width="29.7" height="16.2" fill="#d7262e" stroke="#fff" stroke-width=".3"/><text x="139.1" y="21.8">Unscheduled</text>
        <rect x="154" y="12.9" width="29.7" height="16.2" fill="#d7262e" stroke="#fff" stroke-width=".3"/><text x="168.8" y="21.8">Scheduled</text>
      </g>
    </symbol>
    <symbol id="tum-oper" viewBox="0 0 190 36">
      <g font-family="Arimo,Arial,sans-serif" font-size="2.4" text-anchor="middle">
        <rect x="6" y="15.7" width="59.5" height="6.7" fill="#12262b"/><text x="35.7" y="19.8" fill="#fff">Operating Time</text>
        <rect x="65.5" y="15.7" width="29.1" height="13.4" fill="#3c8a2e"/><text x="80" y="23" fill="#fff">Operating Delay</text>
        <rect x="94.6" y="15.7" width="29.2" height="13.4" fill="#f3e500"/><text x="109.2" y="23" fill="#222">Standby Time</text>
      </g>
    </symbol>
    <symbol id="tum-eff" viewBox="0 0 190 36">
      <g font-family="Arimo,Arial,sans-serif" font-size="2.2" fill="#fff" text-anchor="middle">
        <rect x="6" y="23.5" width="29.8" height="5.6" fill="#12262b" stroke="#fff" stroke-width=".3"/><text x="20.9" y="27">Effective Time</text>
        <rect x="35.8" y="23.5" width="29.7" height="5.6" fill="#6b1f5a" stroke="#fff" stroke-width=".3"/><text x="50.6" y="27">Non-Effective Time</text>
      </g>
    </symbol>
    <symbol id="org" viewBox="0 0 110 32">
      <g stroke="#12262b" stroke-width=".6" fill="none"><path d="M51 9 V14 M28 14 H74 M28 14 V19 M74 14 V19"/></g>
    </symbol>
  </defs>
</svg>

<main class="deck">

<!-- row 1 -->
<section class="slide dark">
  <div class="logo-line" style="left:20px;top:17px;font-size:12px;letter-spacing:.6px">QUENBROOK<i></i></div>
  <div class="sec-h" style="top:49px">VANTRELL BRIGHTPATHS</div>
  <div class="sec-s" style="top:60px">KPIs &amp; Production Fundamentals</div>
  <div style="position:absolute;right:8px;bottom:5px;font-size:1.8px;color:#8d9ca1">© 2024 Quenbrook Mining Solutions Inc. Strictly Confidential</div>
</section>

<section class="slide std">
  <h2 class="ttl">TUM - Summary</h2>
  <svg class="tum" viewBox="0 0 190 36" style="top:25px"><use href="#tum-base"/><use href="#tum-avail"/><use href="#tum-oper"/><use href="#tum-eff"/></svg>
  <ul class="bul" style="left:16px;top:67px;width:190px">
    <li>The Time Usage Model is a way of describing how time for equipment is allocated over a period (shift/month/year)</li>
    <li class="gap">Availability % = What percentage of the shift/month/year is the equipment down?</li>
    <li>Availability % = Available Time / Calendar Time</li>
    <li class="gap">Utilization % = What percentage of the time the equipment is available is it Operating?</li>
    <li>Utilization % = Operating Time / Available Time</li>
  </ul>
  <footer class="foot"><b class="brand">QUENBROOK</b><span class="legal">© 2024 Quenbrook Mining Solutions Inc. Strictly Confidential</span><i class="pg">10</i></footer>
</section>

<section class="slide std">
  <h2 class="ttl">Process Bottleneck – Mine Operations</h2>
  <div class="bn-cap" style="left:53px;top:18px"><i>1</i><span>You add<br>capacity here</span></div>
  <div class="bn-cap" style="left:98px;top:18px"><i>3</i><span>because you're sending<br>more work to the bottleneck</span></div>
  <div class="bn-art" role="img" aria-label="Illustration of a process pipeline with tanks and a narrow bottleneck"></div>
  <span class="bn-tag" style="left:33px;width:20px">Drill &amp; Blast</span>
  <span class="bn-tag" style="left:57px;width:18px">Loading</span>
  <span class="bn-tag" style="left:97px;width:18px">Hauling</span>
  <span class="bn-tag" style="left:136px;width:18px">Crusher</span>
  <span class="bn-tag" style="left:165px;width:14px">Mill</span>
  <div class="bn-cap" style="left:59px;top:93px"><i>2</i><span>but performance<br>here only gets worse</span></div>
  <div class="bn-cap" style="left:140px;top:93px"><i>4</i><span>and system throughput<br>goes down because of<br>added capacity</span></div>
  <footer class="foot"><b class="brand">QUENBROOK</b><span class="legal">© 2024 Quenbrook Mining Solutions Inc. Strictly Confidential</span><i class="pg">19</i></footer>
</section>

<section class="slide std">
  <h2 class="ttl">Theory of Constraints &amp; the SIC Tool</h2>
  <ul class="bul" style="left:15px;top:40px;width:96px;font-size:2.2px">
    <li>The Short Interval Control tool Summary Page shows the capability of the Loading Fleet and Hauling Fleet</li>
    <li>Overtrucked or Undertrucked is based on the capability of the loading fleet or hauling fleet</li>
    <li>Capability is based on</li>
    <li class="sm">Availability</li><li class="sm">Haul Distance</li>
    <li>This gives an average for the shift. Dispatchlink and dispatch can determine if the shift is overtrucked or undertrucked in real-time</li>
    <li>The Truck balance can shift Quickly if a shovel goes down/comes up.</li>
  </ul>
  <svg style="position:absolute;left:120px;top:27px;width:86px;height:86px" viewBox="0 0 86 86" role="img" aria-label="SIC tool summary panel with loading, hauling and truck balance bars">
    <rect x=".5" y=".5" width="85" height="85" fill="#f6f6f6" stroke="#12262b" stroke-width="1.2"/>
    <g font-family="Arimo,Arial,sans-serif" font-size="1.8" fill="#555">
      <text x="4" y="5">Haulage Speed</text><text x="44" y="5">85 %</text>
      <rect x="4" y="7" width="78" height="4" fill="#ccc"/><rect x="4" y="7" width="66" height="4" fill="#f59a00"/>
      <text x="4" y="16">Planned</text><text x="4" y="20">Actual Hauled</text><text x="4" y="24">Truck Hauls</text>
      <text x="4" y="34">Loading Speed</text><text x="44" y="34">74 %</text>
      <rect x="4" y="36" width="78" height="4" fill="#ccc"/><rect x="4" y="36" width="58" height="4" fill="#f59a00"/>
      <text x="4" y="45">Planned</text><text x="4" y="49">Actual Loaded</text><text x="4" y="53">Truck Loads</text>
      <text x="4" y="63">Truck Balance</text><text x="44" y="63">8 %</text>
      <rect x="4" y="65" width="78" height="4" fill="#ccc"/><rect x="37" y="65" width="5" height="4" fill="#3c8a2e"/>
      <text x="35" y="75">Perfect Trucking</text>
    </g>
  </svg>
  <footer class="foot"><b class="brand">QUENBROOK</b><span class="legal">© 2024 Quenbrook Mining Solutions Inc. Strictly Confidential</span><i class="pg">28</i></footer>
</section>

<!-- row 2 -->
<section class="slide std">
  <div class="photo" role="img" aria-label="Photo of a worker in hi-vis beside haul trucks"></div>
  <h2 class="ttl">KPIs &amp; Production<br>Fundamentals</h2>
  <p class="sub" style="left:16px;top:35px">At the end of this module, you will understand</p>
  <div style="position:absolute;left:7px;top:43px;width:118px;height:34px;background:var(--ink);z-index:2"></div>
  <ul class="bul" style="left:13px;top:44px;width:108px;color:#fff;font-size:2px">
    <li>Understand the key concepts of mine production KPIs</li>
    <li>Time Usage Model</li>
    <li class="sm">Availability, Utilization and Productivity</li>
    <li class="sm">Elements of the haul cycle</li>
    <li class="sm">How changes in each of these elements impact production</li>
    <li>The goal will be to create a baseline of understanding and a common language across the entire mine-ops team</li>
    <li>You may already understand these concepts</li>
    <li>This is the time to ask questions and get clarification!</li>
  </ul>
  <footer class="foot"><b class="brand">QUENBROOK</b><span class="legal">© 2024 Quenbrook Mining Solutions Inc. Strictly Confidential</span><i class="pg">2</i></footer>
</section>

<section class="slide std">
  <div class="photo" role="img" aria-label="Photo of a loader filling a haul truck"></div>
  <h2 class="ttl">What Makes up Production</h2>
  <p class="sub" style="left:16px;top:22px">In its simplest terms, we calculate production like this:</p>
  <svg class="org" viewBox="0 0 110 32" style="top:38px"><use href="#org"/>
    <g font-family="Arimo,Arial,sans-serif" font-size="3" fill="#fff" text-anchor="middle">
      <rect x="31" y="0" width="40" height="9" fill="#12262b"/><text x="51" y="5.7">PRODUCTION</text>
      <rect x="10" y="19" width="36" height="10" fill="#d7262e"/><text x="28" y="23.2">Equipment</text><text x="28" y="26.8">Productivity</text>
      <rect x="56" y="19" width="36" height="10" fill="#12262b"/><text x="74" y="23.2">Operating</text><text x="74" y="26.8">Time</text>
    </g>
  </svg>
  <ul class="bul" style="left:15px;top:76px;width:100px;font-size:2.1px">
    <li>The other side of production is Equipment Productivity</li>
    <li>This metric describes how PRODUCTIVE the equipment is during the operating time</li>
    <li>For this course, we will focus on productivity of <b>Trucks and Shovels</b></li>
  </ul>
  <footer class="foot"><b class="brand">QUENBROOK</b><span class="legal">© 2024 Quenbrook Mining Solutions Inc. Strictly Confidential</span><i class="pg">11</i></footer>
</section>

<section class="slide std">
  <h2 class="ttl">Process Bottleneck - Plant</h2>
  <div class="bn-cap" style="left:53px;top:18px"><i>1</i><span>You add<br>capacity here</span></div>
  <div class="bn-cap" style="left:98px;top:18px"><i>3</i><span>because you're sending<br>more work to the bottleneck</span></div>
  <div class="bn-art" role="img" aria-label="Illustration of a plant process pipeline with a narrow bottleneck"></div>
  <span class="bn-tag" style="left:31px;width:24px">Primary Crusher</span>
  <span class="bn-tag" style="left:56px;width:24px">Dome (inventory)</span>
  <span class="bn-tag" style="left:95px;width:22px">Ball + SAG Mill</span>
  <span class="bn-tag" style="left:138px;width:14px">CIP</span>
  <span class="bn-tag" style="left:164px;width:16px">Tailings</span>
  <div class="bn-cap" style="left:59px;top:93px"><i>2</i><span>but performance<br>here only gets worse</span></div>
  <div class="bn-cap" style="left:140px;top:93px"><i>4</i><span>and system throughput<br>goes down because of<br>added capacity</span></div>
  <footer class="foot"><b class="brand">QUENBROOK</b><span class="legal">© 2024 Quenbrook Mining Solutions Inc. Strictly Confidential</span><i class="pg">20</i></footer>
</section>

<section class="slide dark">
  <div class="sec-h">VANTRELL BRIGHTPATHS</div>
  <div class="sec-s" style="top:56px">Expectations for Supervisors and Dispatchers<br>SIC &amp; Visual Management</div>
  <footer class="foot"><b class="brand">QUENBROOK</b><span class="legal" style="margin-left:120px">© 2024 Quenbrook Mining Solutions Inc. Strictly Confidential</span></footer>
</section>

<!-- row 3 -->
<section class="slide std">
  <div class="photo" role="img" aria-label="Photo of an excavator loading a truck"></div>
  <h2 class="ttl">What Makes up Production</h2>
  <p class="sub" style="left:18px;top:22px">In its simplest terms, we calculate production like this:</p>
  <svg class="org" viewBox="0 0 110 32" style="top:40px"><use href="#org"/>
    <g font-family="Arimo,Arial,sans-serif" font-size="3" fill="#fff" text-anchor="middle">
      <rect x="31" y="0" width="40" height="9" fill="#12262b"/><text x="51" y="5.7">PRODUCTION</text>
      <rect x="10" y="19" width="36" height="10" fill="#12262b"/><text x="28" y="23.2">Equipment</text><text x="28" y="26.8">Productivity</text>
      <rect x="56" y="19" width="36" height="10" fill="#12262b"/><text x="74" y="23.2">Operating</text><text x="74" y="26.8">Time</text>
    </g>
  </svg>
  <ul class="bul" style="left:15px;top:91px;width:110px;font-size:2.1px">
    <li>This is true for any process</li>
    <li class="sm">Moving the boxes</li><li class="sm">Driving</li><li class="sm">Mine Production</li>
    <li>Production goes up or down because of a change in <b>Equipment Productivity or Operating Time</b></li>
  </ul>
  <footer class="foot"><b class="brand">QUENBROOK</b><span class="legal">© 2024 Quenbrook Mining Solutions Inc. Strictly Confidential</span><i class="pg">3</i></footer>
</section>

<section class="slide std">
  <div class="photo" role="img" aria-label="Photo of a loaded haul truck"></div>
  <h2 class="ttl">Equipment Productivity –<br>Haul Trucks</h2>
  <svg class="org" viewBox="0 0 110 32" style="top:47px"><use href="#org"/>
    <g font-family="Arimo,Arial,sans-serif" font-size="3" fill="#fff" text-anchor="middle">
      <rect x="21" y="0" width="60" height="9" fill="#12262b"/><text x="51" y="5.7">EQUIPMENT PRODUCTIVITY</text>
      <rect x="10" y="19" width="36" height="9" fill="#12262b"/><text x="28" y="24.6">Cycle Time</text>
      <rect x="56" y="19" width="36" height="9" fill="#d7262e"/><text x="74" y="24.6">Tonnes per Cycle</text>
    </g>
  </svg>
  <ul class="bul" style="left:15px;top:92px;width:110px;font-size:2.1px">
    <li>For haul trucks, tonnes per cycle is simply Payload</li>
    <li>The higher the payload, the higher the equipment productivity</li>
    <li>What are the limitations of Payload?</li>
  </ul>
  <footer class="foot"><b class="brand">QUENBROOK</b><span class="legal">© 2024 Quenbrook Mining Solutions Inc. Strictly Confidential</span><i class="pg">12</i></footer>
</section>

<section class="slide std">
  <h2 class="ttl">Process Bottleneck – Harrow Ridge Mine</h2>
  <div class="bn-cap" style="left:53px;top:18px"><i>1</i><span>You add<br>capacity here</span></div>
  <div class="bn-cap" style="left:98px;top:18px"><i>3</i><span>because you're sending<br>more work to the bottleneck</span></div>
  <div class="bn-art" role="img" aria-label="Illustration of a mine value chain pipeline with a narrow bottleneck"></div>
  <span class="bn-tag" style="left:33px;width:19px">Exploration</span>
  <span class="bn-tag" style="left:58px;width:16px">Mining</span>
  <span class="bn-tag" style="left:100px;width:12px">Mill</span>
  <span class="bn-tag" style="left:136px;width:17px">Tailings</span>
  <span class="bn-tag" style="left:161px;width:22px">Reclamation</span>
  <div class="bn-cap" style="left:59px;top:93px"><i>2</i><span>but performance<br>here only gets worse</span></div>
  <div class="bn-cap" style="left:140px;top:93px"><i>4</i><span>and system throughput<br>goes down because of<br>added capacity</span></div>
  <footer class="foot"><b class="brand">QUENBROOK</b><span class="legal">© 2024 Quenbrook Mining Solutions Inc. Strictly Confidential</span><i class="pg">21</i></footer>
</section>

<section class="slide std">
  <div class="photo" role="img" aria-label="Photo of trucks working in an open pit"></div>
  <h2 class="ttl">Overview – SIC &amp; Visual<br>Management</h2>
  <ul class="bul" style="left:15px;top:36px;width:100px;font-size:2.1px">
    <li>Dispatchers and Pit Supervisors use the SIC tool to monitor the real-time performance of the truck and shovel fleet.</li>
    <li>The tool is monitored hourly to identify underperformance. The dispatcher may be the lead in identifying actions for the Pit Supervisor</li>
    <li>Once opportunities or underperforming areas are identified Dispatchers and Supervisors will take collaborative action to address them</li>
    <li>The Visual Management process is an accountability check and information share. 'Did we monitor the SIC, communicate opportunities and take action during the shift?'</li>
  </ul>
  <footer class="foot"><b class="brand">QUENBROOK</b><span class="legal">© 2024 Quenbrook Mining Solutions Inc. Strictly Confidential</span><i class="pg">30</i></footer>
</section>

<!-- row 4 -->
<section class="slide std">
  <div class="photo" role="img" aria-label="Photo of haul trucks in a mine"></div>
  <h2 class="ttl">What Makes up Production</h2>
  <p class="sub" style="left:18px;top:22px">At its simplest terms, we calculate production like this:</p>
  <svg class="org" viewBox="0 0 110 32" style="top:36px;left:2px"><use href="#org"/>
    <g font-family="Arimo,Arial,sans-serif" font-size="3" fill="#fff" text-anchor="middle">
      <rect x="31" y="0" width="40" height="9" fill="#12262b"/><text x="51" y="5.7">PRODUCTION</text>
      <rect x="10" y="19" width="36" height="10" fill="#12262b"/><text x="28" y="23.2">Equipment</text><text x="28" y="26.8">Productivity</text>
      <rect x="56" y="19" width="36" height="10" fill="#d7262e"/><text x="74" y="23.2">Operating</text><text x="74" y="26.8">Time</text>
    </g>
  </svg>
  <ul class="bul" style="left:15px;top:71px;width:120px;font-size:2.1px">
    <li>Operating time is the time when a piece of equipment is performing it's <b>primary function</b></li>
    <li>To better understand, communicate and discuss the different categories of how we calculate operating time, we use something called a <b>Time Usage Model</b></li>
    <li>Each industry has its own time usage model, and they can vary slightly from industry to industry</li>
    <li>Even within an industry, (e.g. Mining) a Time Usage Model can vary from operation to operation</li>
  </ul>
  <footer class="foot"><b class="brand">QUENBROOK</b><span class="legal">© 2024 Quenbrook Mining Solutions Inc. Strictly Confidential</span><i class="pg">4</i></footer>
</section>

<section class="slide std">
  <h2 class="ttl">Equipment Productivity – Haul Trucks</h2>
  <svg style="position:absolute;left:14px;top:26px;width:200px;height:72px" viewBox="0 0 200 72" role="img" aria-label="Payload distribution curve">
    <defs><linearGradient id="bell" x1="0" x2="1"><stop offset="0" stop-color="#bbb"/><stop offset=".5" stop-color="#555"/><stop offset=".75" stop-color="#888"/><stop offset="1" stop-color="#ccc"/></linearGradient></defs>
    <path d="M18 58 C65 58 80 3 100 3 C120 3 135 58 182 58 Z" fill="url(#bell)"/>
    <path d="M100 3 V58 M150 40 V58" stroke="#222" stroke-width=".6"/>
    <polygon points="40,28 54,17 54,23 98,23 98,33 54,33 54,39" fill="#d8d8d8" stroke="#666" stroke-width=".4"/>
    <text x="74" y="30.5" font-size="5" fill="#fff" font-family="Arimo,Arial,sans-serif" font-weight="700">50 %</text>
    <rect x="8" y="8" width="7" height="40" fill="#12262b"/>
    <text transform="translate(13.3 44) rotate(-90)" font-size="4.2" fill="#fff" font-family="Arimo,Arial,sans-serif">Productivity</text>
    <text transform="translate(5 44) rotate(-90)" font-size="2.2" fill="#333" font-family="Arimo,Arial,sans-serif">Number of Loads</text>
    <rect x="143" y="6" width="7" height="34" fill="#12262b"/>
    <text transform="translate(148.4 36) rotate(-90)" font-size="4.2" fill="#fff" font-family="Arimo,Arial,sans-serif">Durability</text>
    <text x="160" y="46" font-size="5.5" fill="#222" font-weight="700" font-family="Arimo,Arial,sans-serif">10%</text>
    <path d="M18 58 H182" stroke="#222" stroke-width=".4"/>
    <g font-size="2.2" fill="#444" font-family="Arimo,Arial,sans-serif" text-anchor="middle">
      <text x="20" y="63">80</text><text x="40" y="63">85</text><text x="60" y="63">90</text><text x="80" y="63">95</text><text x="100" y="63">100</text><text x="120" y="63">105</text><text x="140" y="63">110</text><text x="160" y="63">115</text>
    </g>
  </svg>
  <ul class="bul" style="left:16px;top:99px;width:195px;font-size:2.2px">
    <li>To increase productivity, we want to maximize truck payload while adhering to the 10/10/20 rule</li>
    <li>No more than <b>10% of loads</b> between <b>110% and 120% of Nominal Payload</b></li>
    <li>No loads greater than <b>120% of Nominal Payload</b></li>
  </ul>
  <footer class="foot"><b class="brand">QUENBROOK</b><span class="legal">© 2024 Quenbrook Mining Solutions Inc. Strictly Confidential</span><i class="pg">13</i></footer>
</section>

<section class="slide std">
  <h2 class="ttl">The Process to Address &amp;<br>Manage Constraints (Bottlenecks)</h2>
  <p class="sub" style="left:17px;top:33px;font-size:2.4px;font-weight:700">The Theory of Constraints is a five-step process:</p>
  <span class="ico" style="left:18px;top:44px"></span>
  <p class="sub" style="left:34px;top:48px;font-size:2px"><b style="color:var(--red);font-size:3px">IDENTIFY</b><br>the process constraint</p>
  <span class="ico" style="left:82px;top:44px"></span>
  <p class="sub" style="left:98px;top:46px;font-size:2px"><b style="color:var(--red);font-size:3px">SUBORDINATE</b><br>everything else to<br>the above decisions.</p>
  <span class="ico" style="left:146px;top:60px"></span>
  <p class="sub" style="left:162px;top:63px;font-size:2px">Remove the constraint and<br><b style="color:var(--red);font-size:3px">RE-EVALUATE</b><br>the process.</p>
  <span class="ico" style="left:18px;top:80px"></span>
  <p class="sub" style="left:34px;top:82px;font-size:2px">Decide how best to<br><b style="color:var(--red);font-size:3px">EXPLOIT</b><br>the process constraints.</p>
  <span class="ico" style="left:82px;top:80px"></span>
  <p class="sub" style="left:98px;top:84px;font-size:2px"><b style="color:var(--red);font-size:3px">ELEVATE</b><br>the process constraint.</p>
  <p class="sub" style="left:150px;top:106px;font-size:1.8px;background:var(--red);color:#fff;padding:.8px 2px">From the book 'The Aim' by Dr. E. Marlowe</p>
  <footer class="foot"><b class="brand">QUENBROOK</b><span class="legal">© 2024 Quenbrook Mining Solutions Inc. Strictly Confidential</span><i class="pg">22</i></footer>
</section>

<section class="slide std">
  <h2 class="ttl">SIC Tool - Expectations</h2>
  <p class="vm-h" style="top:25px;font-size:2.2px">Expectations During the Shift</p>
  <div class="flow" style="left:16px;top:33px">
    <div class="box" style="width:35px;height:20px">All Roles monitor SIC trends for their accountable KPIs – once per hour</div><span class="arw plain">›</span>
    <div class="box" style="width:35px;height:20px">Supervisors actively engage with shovel &amp; support equipment operators</div><span class="arw plain">›</span>
    <div class="box" style="width:55px;height:20px">Dispatchers Monitor Queue and Hang at shovels – take action if opportunities are identified (re-assign trucks, longer hauls, fueling/breaks etc)</div><span class="arw plain">›</span>
    <div class="box" style="width:35px;height:20px">Supervisor Monitors Queue @ Dump, Dumping Times</div>
  </div>
  <div class="flow" style="left:16px;top:57px">
    <div class="box" style="width:35px;height:20px">Controller actively monitors dome levels &amp; queue at the crusher</div><span class="arw plain">›</span>
    <div class="box" style="width:70px;height:20px">Use Monster &amp; SIC Trends to assess the truck balance. Based on the operating scenario (over-trucked or under-trucked) look for opportunities (haul long, haul short, fueling, breaks etc)</div><span class="arw plain">›</span>
    <div class="box" style="width:58px;height:20px">Controllers and Control room supervisors pro-actively communicate with the supervisors on truck/shovel balance and if they see opportunities/issues in their area</div>
  </div>
  <footer class="foot"><b class="brand">QUENBROOK</b><span class="legal">© 2024 Quenbrook Mining Solutions Inc. Strictly Confidential</span><i class="pg">31</i></footer>
</section>

<!-- row 5 -->
<section class="slide std">
  <h2 class="ttl">Generic Time Usage Model</h2>
  <svg class="tum" viewBox="0 0 190 36" style="top:29px"><use href="#tum-base"/><use href="#tum-avail"/><use href="#tum-oper"/><use href="#tum-eff"/></svg>
  <ul class="bul" style="left:16px;top:78px;width:190px;font-size:2.2px">
    <li>This is a generic Mining time usage model</li>
    <li>There may be variations from mine-to-mine (ie Utilized time vs Operating Time) but this model describes everything mine operations need to know about the time usage of a piece of equipment</li>
  </ul>
  <footer class="foot"><b class="brand">QUENBROOK</b><span class="legal">© 2024 Quenbrook Mining Solutions Inc. Strictly Confidential</span><i class="pg">5</i></footer>
</section>

<section class="slide std">
  <h2 class="ttl">Equipment Productivity –<br>Haul Trucks</h2>
  <p class="sub" style="left:16px;top:34px;font-size:2.6px">In its simplest terms,<br>we calculate production like this:</p>
  <ul class="bul" style="left:16px;top:47px;width:68px;font-size:2.1px">
    <li>The first step is to try to reduce non-effective time in a haul cycle</li>
    <li>What are the non-effective elements of the haul cycle?</li>
    <li>What are some ways to reduce non-effective time in a haul cycle?</li>
    <li>What are the effective elements of a haul cycle?</li>
    <li>What are some way to reduce effective time in a haul cycle?</li>
  </ul>
  <svg style="position:absolute;left:90px;top:14px;width:126px;height:102px" viewBox="0 0 126 102" role="img" aria-label="Haul truck cycle: stopped, loading, travelling full, dumping, travelling empty">
    <ellipse cx="63" cy="52" rx="55" ry="44" fill="none" stroke="#555" stroke-width=".5" stroke-dasharray="1.5 1"/>
    <g fill="none" stroke="#d7262e" stroke-width=".8">
      <path d="M40 16 C46 12 52 10 58 10"/><path d="M106 40 C108 44 108 48 106 52"/><path d="M100 62 C96 66 90 68 84 70"/>
      <path d="M60 86 C52 86 46 84 40 82"/><path d="M26 62 C22 58 20 50 22 44"/>
    </g>
    <g font-family="Arimo,Arial,sans-serif" font-size="2.1" fill="#333" text-anchor="middle">
      <text x="67" y="17">Stopped</text><text x="67" y="19.5">Empty</text>
      <text x="67" y="32">Travelling</text><text x="67" y="34.5">Empty</text>
      <text x="104" y="37">Wait/Queue</text><text x="104" y="39.5">at Shovel</text>
      <text x="28" y="45">Stopped Full</text>
      <text x="100" y="62">Spotting</text>
      <text x="92" y="76">Loading</text>
      <text x="70" y="76">Travelling Full</text>
      <text x="24" y="62">Wait/Queue</text><text x="24" y="64.5">at Dump</text>
      <text x="40" y="91">Stopped</text><text x="40" y="93.5">Full</text>
    </g>
  </svg>
  <footer class="foot"><b class="brand">QUENBROOK</b><span class="legal">© 2024 Quenbrook Mining Solutions Inc. Strictly Confidential</span><i class="pg">14</i></footer>
</section>

<section class="slide std">
  <h2 class="step-h">The ToC Process:</h2>
  <div class="step-tag">Step 1</div>
  <span class="step-ico"></span>
  <p class="step-t">IDENTIFY the Process<br>Constraint</p>
  <p class="step-q" style="top:62px">How to Identify The Process Constraint or Bottleneck</p>
  <div class="flow" style="left:34px;top:72px">
    <div class="box" style="width:38px;height:27px">The step in the process that never seems to stop, always trying to catch up</div><span class="arw">›</span>
    <div class="box" style="width:38px;height:27px">Observation – look for the points in the process with large numbers of "things" piled up at the input.</div><span class="arw">›</span>
    <div class="box" style="width:30px;height:27px">Look at the capability (TPOH) of that step in the process</div>
  </div>
  <footer class="foot"><b class="brand">QUENBROOK</b><span class="legal">© 2024 Quenbrook Mining Solutions Inc. Strictly Confidential</span><i class="pg">23</i></footer>
</section>

<section class="slide std">
  <h2 class="ttl">Visual Management – Process</h2>
  <p class="vm-h" style="top:25px;font-size:2.2px">Visual Management Meeting - 5:00 AM, 12:00 PM and 5:00 PM</p>
  <div class="flow" style="left:16px;top:33px">
    <div class="box" style="width:40px;height:21px">The goal is for the meeting to take 10 minutes only</div><span class="arw plain">›</span>
    <div class="box" style="width:40px;height:21px">Attendees should come prepared</div><span class="arw plain">›</span>
    <div class="box" style="width:100px;height:21px">Understand the operating scenario – over-trucked or under-trucked, crusher status, etc. What strategies should be employed based on the operations playbook</div>
  </div>
  <div class="flow" style="left:16px;top:59px">
    <div class="box" style="width:40px;height:21px">Review Visual Management Slides in Order</div><span class="arw plain">›</span>
    <div class="box" style="width:40px;height:21px">Review red KPIs, move past green ones</div><span class="arw plain">›</span>
    <div class="box" style="width:45px;height:21px">Not a deep dive or time to investigate SIC trends</div><span class="arw plain">›</span>
    <div class="box" style="width:46px;height:21px">Focus on identifying issues and taking action</div>
  </div>
  <footer class="foot"><b class="brand">QUENBROOK</b><span class="legal">© 2024 Quenbrook Mining Solutions Inc. Strictly Confidential</span><i class="pg">32</i></footer>
</section>

<!-- row 6 -->
<section class="slide std">
  <h2 class="ttl">TUM – Calendar Time</h2>
  <svg class="tum" viewBox="0 0 190 36" style="top:25px;height:40px" preserveAspectRatio="none"><use href="#tum-base"/><polygon points="82,36 95,12 108,36" fill="#fff"/></svg>
  <ul class="bul" style="left:16px;top:81px;width:160px;font-size:2.2px">
    <li>Calendar time means all the time in a period</li>
    <li class="sm">Calendar time for 1 Year = 365 Days</li>
    <li class="sm">Calendar time for October = 31 days</li>
    <li class="sm">Calendar time for 1 shift = 12 hours</li>
  </ul>
  <footer class="foot"><b class="brand">QUENBROOK</b><span class="legal">© 2024 Quenbrook Mining Solutions Inc. Strictly Confidential</span><i class="pg">6</i></footer>
</section>

<section class="slide dark">
  <div class="sec-h" style="top:46px">VANTRELL BRIGHTPATHS</div>
  <div class="sec-s" style="top:57px">The Theory of Constraints</div>
  <footer class="foot"><b class="brand">QUENBROOK</b><span class="legal" style="margin-left:120px">© 2024 Quenbrook Mining Solutions Inc. Strictly Confidential</span></footer>
</section>

<section class="slide std">
  <h2 class="step-h">The ToC Process:</h2>
  <div class="step-tag">Step 2</div>
  <span class="step-ico"></span>
  <p class="step-t">EXPLOIT the Process<br>Constraint</p>
  <p class="step-q" style="top:56px">Decide how to exploit the constraint –<br>Make the constraint as productive as possible</p>
  <p class="step-e" style="top:69px">Examples might include:</p>
  <div class="flow" style="left:34px;top:79px">
    <div class="box" style="width:28px;height:26px">Making sure it works as consistently as possible</div><span class="arw">›</span>
    <div class="box" style="width:28px;height:26px">Never has to take breaks, or as infrequently as possible</div><span class="arw">›</span>
    <div class="box" style="width:28px;height:26px">If interruptions have to occur, try to have multiple at the same time</div><span class="arw">›</span>
    <div class="box" style="width:28px;height:26px">Cross train employees to provide for shifting resources when volume exceeds the capability of the constraint.</div>
  </div>
  <footer class="foot"><b class="brand">QUENBROOK</b><span class="legal">© 2024 Quenbrook Mining Solutions Inc. Strictly Confidential</span><i class="pg">24</i></footer>
</section>

<section class="slide std">
  <h2 class="ttl">Visual Management</h2>
  <p class="vm-h" style="top:25px;font-size:2.2px">Expectations @ Visual Management Meeting – Senior Supervisors</p>
  <div class="flow" style="left:16px;top:33px">
    <div class="box" style="width:33px;height:21px">Senior Supervisors own the meeting</div><span class="arw plain">›</span>
    <div class="box" style="width:50px;height:21px">Review the SIC prior to the meeting – Quenbrook to support</div><span class="arw plain">›</span>
    <div class="box" style="width:55px;height:21px">Set expectations and hold Dispatchers &amp; Supervisors accountable</div><span class="arw plain">›</span>
    <div class="box" style="width:29px;height:21px">Keep process on track</div>
  </div>
  <div class="flow" style="left:16px;top:59px">
    <div class="box" style="width:33px;height:21px">Stay out of trends/details</div><span class="arw plain">›</span>
    <div class="box" style="width:80px;height:21px">Reset expectations and speak straight, respectfully if expectations aren't met</div><span class="arw plain">›</span>
    <div class="box" style="width:60px;height:21px">Celebrate Success and provide positive reinforcement</div>
  </div>
  <footer class="foot"><b class="brand">QUENBROOK</b><span class="legal">© 2024 Quenbrook Mining Solutions Inc. Strictly Confidential</span><i class="pg">33</i></footer>
</section>

<!-- row 7 -->
<section class="slide std">
  <h2 class="ttl">TUM – Available Time</h2>
  <svg class="tum" viewBox="0 0 190 36" style="top:24px;height:40px" preserveAspectRatio="none"><use href="#tum-base"/><use href="#tum-avail"/><polygon points="82,36 95,16 108,36" fill="#fff"/></svg>
  <ul class="bul" style="left:16px;top:70px;width:190px;font-size:2.2px">
    <li>Available Time is the time a piece of equipment (or fleet) is mechanically available to operate</li>
    <li>Available Time = Calendar Time – Down Time</li>
    <li>Downtime can be</li>
    <li class="sm">Planned (PMs, Rebuilds)</li>
    <li class="sm">Unplanned (Breakdown, Accident Damage)</li>
    <li>Availability % = Available Time / Calendar Time</li>
  </ul>
  <footer class="foot"><b class="brand">QUENBROOK</b><span class="legal">© 2024 Quenbrook Mining Solutions Inc. Strictly Confidential</span><i class="pg">7</i></footer>
</section>

<section class="slide std">
  <div class="photo" role="img" aria-label="Photo of a shovel working on a mine bench"></div>
  <h2 class="ttl">Objectives</h2>
  <p class="sub" style="left:16px;top:22px;font-size:2.3px;font-weight:700">At the conclusion of this module, you will be able to:</p>
  <div class="obj" style="top:37px"><span></span><p>Understand<br>the Theory Of Constraints.</p></div>
  <div class="obj" style="top:59px"><span></span><p>Apply the principles of<br>the Theory of Constraints<br>to Truck &amp; Shovel Operations</p></div>
  <div class="obj" style="top:82px"><span></span><p>Understand how<br>we can practically use<br>this information to take action in the mine</p></div>
  <footer class="foot"><b class="brand">QUENBROOK</b><span class="legal">© 2024 Quenbrook Mining Solutions Inc. Strictly Confidential</span><i class="pg">16</i></footer>
</section>

<section class="slide std">
  <h2 class="step-h">The ToC Process:</h2>
  <div class="step-tag">Step 3</div>
  <span class="step-ico"></span>
  <p class="step-t">SUBORDINATE<br>Everything Else</p>
  <p class="step-q" style="top:64px">Subordinate everything else to the process constraint</p>
  <div class="flow" style="left:34px;top:74px">
    <div class="box" style="width:28px;height:26px">An hour lost at the constraint is an hour lost in the entire process.</div><span class="arw">›</span>
    <div class="box" style="width:28px;height:26px">The constraint is, therefore, the top priority</div><span class="arw">›</span>
    <div class="box" style="width:28px;height:26px">It should never be idle; resources should never be taken from the constraint to work on other priorities</div><span class="arw">›</span>
    <div class="box" style="width:28px;height:26px">Other processes can be made less efficient if it is <b>Better for the Contraint</b></div>
  </div>
  <footer class="foot"><b class="brand">QUENBROOK</b><span class="legal">© 2024 Quenbrook Mining Solutions Inc. Strictly Confidential</span><i class="pg">25</i></footer>
</section>

<section class="slide std">
  <div class="photo" role="img" aria-label="Photo of two supervisors in hard hats on site"></div>
  <h2 class="ttl">Visual Management</h2>
  <p class="sub" style="left:17px;top:26px;font-size:2.1px;font-weight:700">Expectations @ Visual Management Meeting –<br>Dispatchers &amp; Supervisors</p>
  <ul class="bul" style="left:16px;top:36px;width:90px;font-size:2.1px">
    <li>For each KPI they are accountable for Dispatcher and Supervisors must report</li>
    <li class="sm">What happened during the shift – Good, bad and change in KPI</li>
    <li class="sm">When was issue identified</li>
    <li class="sm">What communication &amp; actions did you take</li>
    <li class="sm">Did it improve</li>
    <li class="sm">How will KPI look going forward</li>
    <li class="sm">Any other actions required</li>
    <li>If you are monitoring the SIC during the shift it is easy to answer these questions</li>
  </ul>
  <footer class="foot"><b class="brand">QUENBROOK</b><span class="legal">© 2024 Quenbrook Mining Solutions Inc. Strictly Confidential</span><i class="pg">34</i></footer>
</section>

<!-- row 8 -->
<section class="slide std">
  <h2 class="ttl">TUM – Operating Time</h2>
  <svg class="tum" viewBox="0 0 190 36" style="top:25px"><use href="#tum-base"/><use href="#tum-avail"/><use href="#tum-oper"/></svg>
  <ul class="bul" style="left:16px;top:66px;width:192px;font-size:2.1px">
    <li><b>Operating Time is the time where the equipment (or fleet) is running as planned</b></li>
    <li>It excludes periods of standby and operating delays</li>
    <li>Standby time is typically time where the piece of equipment isn't required to operate</li>
    <li class="sm">This could be because there isn't work to do (No Shovel, No Hauls)</li>
    <li class="sm">It could also be because there is nobody to operate the machine (No Operator)</li>
    <li>Operating Delay occurs when the equipment is required to operate but can't perform it's primary work function</li>
    <li class="sm">Fueling, Tramming, Moving</li>
    <li class="sm">As a rule of thumb, if there is a fault in the task, it's considered an operating delay, not a standby</li>
    <li>Utilization % = Operating Time / Available Time</li>
    <li>Some sites refer to this as Use of Availability % or UofA %</li>
  </ul>
  <footer class="foot"><b class="brand">QUENBROOK</b><span class="legal">© 2024 Quenbrook Mining Solutions Inc. Strictly Confidential</span><i class="pg">8</i></footer>
</section>

<section class="slide std">
  <div class="photo night" role="img" aria-label="Night photo of an open pit mine"></div>
  <h2 class="ttl">Theory of Constraints<br>(ToC)</h2>
  <div style="position:absolute;left:20px;top:43px;width:31px;height:58px;background:var(--ink-2);border-radius:3px;color:#fff;font-size:2px;line-height:1.35;text-align:center;padding:3px 2px;z-index:3">Simply put, the theory of constraints states that the throughput of a given process with multiple sequential steps is determined by the one step that takes the most time to complete.<br><br>The step is referred to as the bottleneck</div>
  <footer class="foot"><b class="brand">QUENBROOK</b><span class="legal">© 2024 Quenbrook Mining Solutions Inc. Strictly Confidential</span><i class="pg">17</i></footer>
</section>

<section class="slide std">
  <h2 class="step-h">The ToC Process:</h2>
  <div class="step-tag">Step 4</div>
  <span class="step-ico"></span>
  <p class="step-t">ELEVATE the Process<br>Constraint</p>
  <p class="step-q" style="top:56px">Elevate the process constraint –<br>determine how to remove the constraint.</p>
  <p class="step-e" style="top:69px">Examples might include:</p>
  <div class="flow" style="left:34px;top:79px">
    <div class="box" style="width:28px;height:26px">Reduce queue times</div><span class="arw">›</span>
    <div class="box" style="width:28px;height:26px">Reduce maintenance times</div><span class="arw">›</span>
    <div class="box" style="width:28px;height:26px">Reduce setup / work preparation time</div><span class="arw">›</span>
    <div class="box" style="width:28px;height:26px">Reduce the time required to complete the task (usually a small percentage of the cycle time)</div>
  </div>
  <footer class="foot"><b class="brand">QUENBROOK</b><span class="legal">© 2024 Quenbrook Mining Solutions Inc. Strictly Confidential</span><i class="pg">26</i></footer>
</section>

<section class="slide dark">
  <div class="logo-line" style="left:66px;top:43px;font-size:13px;letter-spacing:.6px">QUENBROOK<i></i></div>
  <div style="position:absolute;left:0;right:0;top:62px;text-align:center;color:var(--red);font-weight:700;font-size:18px;letter-spacing:.3px">THANK YOU</div>
</section>

<!-- row 9 -->
<section class="slide std">
  <h2 class="ttl">TUM – Effective Time</h2>
  <svg class="tum" viewBox="0 0 190 36" style="top:25px"><use href="#tum-base"/><use href="#tum-avail"/><use href="#tum-oper"/><use href="#tum-eff"/></svg>
  <ul class="bul" style="left:16px;top:66px;width:192px;font-size:2.1px">
    <li><b>Effective Time is the time when the equipment is doing its productive activities</b></li>
    <li>It excludes waiting/idle time that is included in operating time</li>
    <li>This waiting/idle, non-effective time is a part of the regular operation of the machine, but is not productive</li>
    <li class="sm">Queuing</li>
    <li class="sm">Truck wait @ dump or wait @ shovel</li>
    <li>Effective Utilization % = Effective Time / Available Time</li>
    <li>OEE % = Effective Time / Calendar Time</li>
  </ul>
  <footer class="foot"><b class="brand">QUENBROOK</b><span class="legal">© 2024 Quenbrook Mining Solutions Inc. Strictly Confidential</span><i class="pg">9</i></footer>
</section>

<section class="slide std">
  <h2 class="ttl">Process Bottleneck</h2>
  <div class="bn-cap" style="left:53px;top:18px"><i>1</i><span>You add<br>capacity here</span></div>
  <div class="bn-cap" style="left:98px;top:18px"><i>3</i><span>because you're sending<br>more work to the bottleneck</span></div>
  <div class="bn-art" role="img" aria-label="Illustration of a generic process pipeline with a narrow bottleneck"></div>
  <div class="bn-cap" style="left:59px;top:89px"><i>2</i><span>but performance<br>here only gets worse</span></div>
  <div class="bn-cap" style="left:140px;top:89px"><i>4</i><span>and system throughput<br>goes down because of<br>added capacity</span></div>
  <footer class="foot"><b class="brand">QUENBROOK</b><span class="legal">© 2024 Quenbrook Mining Solutions Inc. Strictly Confidential</span><i class="pg">18</i></footer>
</section>

<section class="slide std">
  <h2 class="step-h">The ToC Process:</h2>
  <div class="step-tag">Step 5</div>
  <span class="step-ico"></span>
  <p class="step-t">RE-EVALUATE<br>the Process</p>
  <div class="flow" style="left:34px;top:60px">
    <div class="box" style="width:28px;height:26px">Once you have removed a constraint, you have created another.</div><span class="arw">›</span>
    <div class="box" style="width:28px;height:26px">There will always be a slower / less productive process step, and the chain is only as strong as the weakest link</div><span class="arw">›</span>
    <div class="box" style="width:28px;height:26px">Return to step one and identify the new constraint.</div>
  </div>
  <footer class="foot"><b class="brand">QUENBROOK</b><span class="legal">© 2024 Quenbrook Mining Solutions Inc. Strictly Confidential</span><i class="pg">27</i></footer>
</section>

</main>
</body>
</html>
```